Marvantar - Seafood industry professional promoting page

Hi. I´m in the seafood business with a one man company sourcing and exporting frozen seafood. I need to make a one page homepage for Marvantar (from Iceland). The feeling of it should be; Trustworthy, experience and knowledge.
Using as background a picture (or part of it), or a moving video:

http://www1.brelvik.is/sjorinn/myndir/ufsinn.jpg
https://clipvera.com/583720415

Main text to be:

- We can help source, market and add value to your seafood business
- Years of experience in seafood trade and production
- Extensive knowledge of fishing, seasonality, production and accreditations

Contact:
dagur@marvantar.is
Tel: +3654170392
(with a photo)

p.s. please also make logo look better.

Target Market(s)

Seafood industry

Industry/Entity Type

Business

Logo Text

Marvantar

Coding

Coded - Design and coding required

Number of Pages Required

1 page

Colors
0792cd
33a6d7

```html
<!DOCTYPE html>
<html lang="en">
<head>
<meta charset="utf-8">
<title>Marvantar – Seafood sourcing and export</title>
<link rel="stylesheet" href="https://fonts.googleapis.com/css2?family=Open+Sans:wght@300;400;600;700&family=Merriweather:wght@300;400&display=swap">
<style>
:root{
  --navy:#1b2a6b;
  --navy-deep:#141c4e;
  --blue:#0792cd;
  --blue-light:#33a6d7;
  --button:#3a7fdc;
  --hero-top:#0b4fa0;
  --hero-bottom:#083f8c;
  --rose:#a8456f;
  --violet:#3b3a8f;
  --grey-bg:#eeeeee;
  --field:#f0f0f0;
  --text:#2b3a7a;
  --white:#ffffff;
}
*{margin:0;padding:0;box-sizing:border-box}
html,body{width:1200px;height:3579px;overflow:hidden}
body{position:relative;background:var(--white);font-family:"Open Sans",Arial,sans-serif;color:var(--text)}
.abs{position:absolute}

/* navigation bar */
.navbar{position:absolute;left:0;width:1200px;background:var(--white);display:flex;align-items:center;border-bottom:1px solid #e3e3e3}
.navbar .brand{position:absolute;left:48px;display:flex;align-items:center;gap:10px;font-weight:700;color:var(--navy);letter-spacing:1px}
.navbar .brand .dot{border-radius:50%;background:var(--blue)}
.navbar .links{position:absolute;right:59px;display:flex;align-items:center;gap:22px;font-size:10px;color:var(--button)}
.navbar .cta{background:var(--button);color:var(--white);border-radius:14px;padding:5px 16px;font-size:11px}
.nav-main{top:0;height:72px}
.nav-main .brand{font-size:24px}
.nav-main .brand .dot{width:28px;height:28px}
.nav-sticky{height:45px}
.nav-sticky .brand{font-size:15px}
.nav-sticky .brand .dot{width:18px;height:18px}

/* image bands */
.band{position:absolute;left:0;width:1200px}
.band .headline{position:absolute;left:310px;color:var(--white);font-weight:300;font-size:43px;line-height:52px}
.hero{top:72px;height:539px;background:linear-gradient(180deg,var(--hero-top),var(--hero-bottom))}
.hero .headline{top:131px;width:600px}
.hero .actions{position:absolute;left:315px;top:303px;display:flex;gap:16px}
.btn{width:114px;height:32px;border-radius:16px;font-size:11px;color:var(--white);display:flex;align-items:center;justify-content:center}
.btn-fill{background:var(--button)}
.btn-line{border:1.5px solid var(--white)}
.catch{top:1267px;height:565px;background:linear-gradient(180deg,#a7406e 0%,#6a3f84 55%,var(--violet) 100%)}
.catch .headline{top:205px}
.harbour{top:2486px;height:563px;background:linear-gradient(180deg,var(--rose) 0%,#6a3e85 55%,#33388f 100%)}
.harbour .headline{top:179px}

/* round buttons */
.round{position:absolute;width:38px;height:38px;border-radius:50%;display:flex;align-items:center;justify-content:center}
.round.dark{background:rgba(20,28,78,.45)}
.round.grey{background:#a6a6a6}

/* text sections */
.intro{position:absolute;left:0;width:1200px;text-align:center}
.intro h2{font-weight:300;font-size:33px;color:var(--navy)}
.intro .rule{width:80px;height:2px;background:var(--navy);margin:14px auto 14px}
.intro p{font-family:"Merriweather",Georgia,serif;font-size:11.5px;line-height:17px;color:var(--text);width:640px;margin:0 auto}
.story{top:838px}
.why{top:2060px}

/* contact */
.contact{position:absolute;left:0;top:3049px;width:1200px;height:449px;background:var(--grey-bg)}
.portrait{position:absolute;left:250px;top:55px;width:175px;height:308px;background:linear-gradient(180deg,#a9b6c4 0%,#6d7d8c 55%,#26313a 100%)}
.details{position:absolute;left:446px;top:55px;color:var(--blue-light)}
.details h3{font-weight:400;font-size:15px;color:var(--button);margin-bottom:10px}
.details .row{display:flex;align-items:center;gap:14px;font-size:16px;color:var(--button);margin-bottom:8px}
.form-card{position:absolute;left:725px;top:53px;width:215px;height:310px;background:var(--white);box-shadow:0 1px 4px rgba(0,0,0,.15);padding:22px 20px}
.form-card h4{font-weight:400;font-size:14px;color:#333;margin-bottom:14px}
.field{background:var(--field);height:36px;margin-bottom:10px;font-family:"Merriweather",Georgia,serif;font-size:10px;color:#999;padding:11px 10px}
.field.tall{height:82px}
.send{margin:20px auto 0;width:134px;height:30px;border-radius:15px;background:var(--button);color:var(--white);font-size:10px;display:flex;align-items:center;justify-content:center;letter-spacing:.5px}

/* footer */
.footer{position:absolute;left:0;top:3498px;width:1200px;height:81px;background:var(--navy-deep);color:var(--white)}
.footer .brand{position:absolute;left:322px;top:28px;font-size:17px;display:flex;align-items:center;gap:10px}
.footer .brand .dot{width:18px;height:18px;border-radius:50%;background:var(--white)}
.footer .copy{position:absolute;left:537px;top:34px;font-size:9px;opacity:.85}
.footer .social{position:absolute;left:853px;top:34px;width:12px;height:12px;border-radius:50%;background:var(--white)}
</style>
</head>
<body>

<header class="navbar nav-main">
  <div class="brand"><span class="dot"></span>MARVANTAR</div>
  <nav class="links"><span>Our Story</span><span>Why Marvantar</span><span class="cta">Contact Us</span></nav>
</header>

<section class="band hero" role="img" aria-label="Blue-toned photograph of fish underwater">
  <h1 class="headline">We can help source, market and add value to your seafood business</h1>
  <div class="actions"><span class="btn btn-fill">Read More</span><span class="btn btn-line">Contact us</span></div>
  <span class="round dark" style="left:582px;top:472px">
    <svg width="16" height="16" viewBox="0 0 16 16"><path d="M8 2v11M3 8l5 5 5-5" stroke="#fff" stroke-width="1.5" fill="none"/></svg></span>
</section>

<section class="intro story">
  <h2>Our Story</h2>
  <div class="rule"></div>
  <p>Marvantar celebrates GREAT seafood. We serve the finest, most discerning restaurants, nationwide, by delivering fresh seafood every day. We are experts in the industry. We simply believe in sourcing and offering the best frozen seafood, period.</p>
</section>
<span class="round grey" style="left:587px;top:1152px">
  <svg width="16" height="16" viewBox="0 0 16 16"><path d="M8 2v11M3 8l5 5 5-5" stroke="#fff" stroke-width="1.5" fill="none"/></svg></span>

<header class="navbar nav-sticky" style="top:1222px">
  <div class="brand"><span class="dot"></span>MARVANTAR</div>
  <nav class="links"><span>Our Story</span><span>Why Marvantar</span><span class="cta">Contact Us</span></nav>
</header>

<section class="band catch" role="img" aria-label="Close-up photograph of fresh whole fish on ice, rose and violet tint">
  <h2 class="headline">Experienced in seafood trade<br>and production</h2>
  <span class="round dark" style="left:582px;top:494px">
    <svg width="16" height="16" viewBox="0 0 16 16"><path d="M8 2v11M3 8l5 5 5-5" stroke="#fff" stroke-width="1.5" fill="none"/></svg></span>
  <span class="round dark" style="left:1105px;top:508px">
    <svg width="16" height="16" viewBox="0 0 16 16"><path d="M8 14V3M3 8l5-5 5 5" stroke="#fff" stroke-width="1.5" fill="none"/></svg></span>
</section>

<section class="intro why">
  <h2>Why Marvantar</h2>
  <div class="rule"></div>
  <p>We wanted to share GREAT seafood with individuals nationwide.<br>Marvantar strives to deliver a little escape in every box with seasonally exceptional seafood and a hand selected accompaniment.</p>
</section>
<span class="round grey" style="left:587px;top:2372px">
  <svg width="16" height="16" viewBox="0 0 16 16"><path d="M8 2v11M3 8l5 5 5-5" stroke="#fff" stroke-width="1.5" fill="none"/></svg></span>

<header class="navbar nav-sticky" style="top:2443px">
  <div class="brand"><span class="dot"></span>MARVANTAR</div>
  <nav class="links"><span>Our Story</span><span>Why Marvantar</span><span class="cta">Contact Us</span></nav>
</header>

<section class="band harbour" role="img" aria-label="Photograph of fishing boats moored in a harbour, rose and violet tint">
  <h2 class="headline">Extensive knowledge of<br>fishing, seasonality,<br>production and accreditations</h2>
  <span class="round dark" style="left:582px;top:494px">
    <svg width="16" height="16" viewBox="0 0 16 16"><path d="M8 2v11M3 8l5 5 5-5" stroke="#fff" stroke-width="1.5" fill="none"/></svg></span>
  <span class="round dark" style="left:1105px;top:511px">
    <svg width="16" height="16" viewBox="0 0 16 16"><path d="M8 14V3M3 8l5-5 5 5" stroke="#fff" stroke-width="1.5" fill="none"/></svg></span>
</section>

<section class="contact">
  <div class="portrait" role="img" aria-label="Photograph of a fisherman in waders standing in a lake, seen from behind"></div>
  <div class="details">
    <h3>Contact us</h3>
    <div class="row">
      <svg width="20" height="14" viewBox="0 0 20 14"><rect x="1" y="1" width="18" height="12" fill="none" stroke="#3a7fdc" stroke-width="1.3"/><path d="M1 1l9 7 9-7" fill="none" stroke="#3a7fdc" stroke-width="1.3"/></svg>
      dagur@marvantar.is</div>
    <div class="row">
      <svg width="20" height="20" viewBox="0 0 20 20"><rect x="5" y="1" width="10" height="18" rx="2" fill="none" stroke="#3a7fdc" stroke-width="1.3"/><line x1="8.5" y1="16" x2="11.5" y2="16" stroke="#3a7fdc" stroke-width="1.3"/></svg>
      +365 417 0392</div>
  </div>
  <div class="form-card">
    <h4>Ready to get started?</h4>
    <div class="field">Your Name</div>
    <div class="field">Email</div>
    <div class="field tall">Message</div>
    <div class="send">SEND MESSAGE</div>
  </div>
</section>

<footer class="footer">
  <div class="brand"><span class="dot"></span>Marvantar</div>
  <div class="copy">© Copyright 2018 Marvantar - All Rights Reserved</div>
  <span class="social"></span>
  <span class="round" style="left:1105px;top:22px">
    <svg width="16" height="16" viewBox="0 0 16 16"><path d="M8 14V3M3 8l5-5 5 5" stroke="#fff" stroke-width="1.5" fill="none"/></svg></span>
</footer>

</body>
</html>
```